Professional & attention grabbing.

A business card design, front and back. I already have a logo I will attach, but I am open to something new as well.
Things to include:
Name:
Title:
Phone:
Email:
Wanting something that is professional but attention grabbing.
Also we do a lot of work using drones on natural gas pipelines (leading the future)if you want to include any of that. I'm open to ideas.
Target Market(s)
Natural gas transmission industry / greenhouse gas mitigation industry
Industry/Entity Type
Business
Contact Information for Business Card
All details have been conveyed above.
Colors
Designer to choose colors to be used in the design.
Look and feel
Each slider illustrates characteristics of the customer's brand and the style your logo design should communicate.

```html
<!DOCTYPE html>
<html lang="en">
<head>
<meta charset="utf-8">
<title>Halvard Inspections – Business Card</title>
<link rel="stylesheet" href="https://fonts.googleapis.com/css2?family=Arimo:wght@400;700&family=Tinos&display=swap">
<style>
  :root {
    --red: #c0202a;
    --red-dark: #9e1820;
    --ink: #2b2b2d;
    --paper: #ffffff;
    --backdrop: #e4e6e8;
    --pipe-light: #e8a89a;
    --pipe-mid: #c9665c;
    --pipe-deep: #8e3a38;
  }
  * { box-sizing: border-box; margin: 0; padding: 0; }
  html, body { width: 1200px; height: 777px; overflow: hidden; }
  body {
    background: var(--backdrop);
    font-family: "Arimo", Arial, sans-serif;
    position: relative;
  }
  .card {
    position: absolute;
    top: 238px;
    width: 520px;
    height: 300px;
    background: var(--paper);
    box-shadow: 0 6px 18px rgba(0,0,0,.18);
    overflow: hidden;
  }
  .card--front { left: 50px; }
  .card--back { left: 630px; }

  /* front */
  .front-art { position: absolute; inset: 0; width: 100%; height: 100%; }
  .front-brand {
    position: absolute; top: 24px; left: 0; right: 0;
    display: flex; align-items: center; justify-content: center; gap: 10px;
  }
  .brand-square { width: 22px; height: 22px; background: var(--red); }
  .brand-name {
    font-weight: 700; font-size: 40px; letter-spacing: 1px; color: var(--ink); line-height: 1;
  }
  .front-title {
    position: absolute; top: 218px; left: 0; right: 0; text-align: center;
    font-weight: 700; font-size: 26px; color: var(--red); letter-spacing: .5px;
  }

  /* back */
  .back-info { position: absolute; left: 30px; top: 36px; width: 250px; }
  .back-company {
    font-size: 21px; color: var(--red); line-height: 1.05; text-transform: uppercase;
  }
  .back-company span { display: block; padding-left: 24px; }
  .back-tagline {
    display: inline-block; margin-left: 24px; margin-top: 3px;
    background: var(--red); color: var(--paper);
    font-family: "Tinos", "Times New Roman", serif; font-size: 11px; padding: 1px 6px;
  }
  .contact-list { list-style: none; margin-top: 30px; }
  .contact-item {
    display: flex; align-items: center; gap: 10px; margin-bottom: 16px;
    font-weight: 700; font-size: 12px; color: var(--red); line-height: 1.2;
  }
  .contact-icon {
    flex: none; width: 20px; height: 20px; border-radius: 50%;
    background: var(--red); display: flex; align-items: center; justify-content: center;
  }
  .brand-panel {
    position: absolute; left: 298px; top: 0; width: 185px; height: 100%;
    background: var(--red);
    display: flex; align-items: center; justify-content: center; gap: 10px;
  }
  .brand-panel .brand-square { background: var(--paper); }
  .brand-panel .brand-name { color: var(--paper); }
</style>
</head>
<body>

<section class="card card--front">
  <svg class="front-art" viewBox="0 0 520 300" preserveAspectRatio="none">
    <defs>
      <linearGradient id="pipeTone" x1="0" y1="0" x2="1" y2="1">
        <stop offset="0" stop-color="var(--pipe-deep)"/>
        <stop offset=".45" stop-color="var(--pipe-light)"/>
        <stop offset="1" stop-color="var(--pipe-mid)"/>
      </linearGradient>
    </defs>
    <path d="M0 88 Q260 118 520 84 L520 108 Q260 142 0 112 Z" fill="var(--red)"/>
    <path d="M0 100 Q260 132 520 96 L520 196 Q260 166 0 200 Z" fill="url(#pipeTone)" role="img" aria-label="Close-up photograph of natural gas pipeline sections"/>
    <path d="M0 196 Q260 162 520 192 L520 206 Q260 178 0 210 Z" fill="var(--red)"/>
    <path d="M0 276 Q260 258 520 280 L520 300 L0 300 Z" fill="var(--red)"/>
  </svg>
  <div class="front-brand">
    <span class="brand-square"></span>
    <span class="brand-name">HVR</span>
  </div>
  <h1 class="front-title">HALVARD INSPECTIONS</h1>
</section>

<section class="card card--back">
  <div class="back-info">
    <h2 class="back-company">Halvard<span>Inspections</span></h2>
    <p class="back-tagline">Natural gas transmission industry</p>
    <ul class="contact-list">
      <li class="contact-item">
        <span class="contact-icon"><svg width="10" height="12" viewBox="0 0 10 12"><path d="M5 0a4 4 0 0 1 4 4c0 3-4 8-4 8S1 7 1 4a4 4 0 0 1 4-4z" fill="#fff"/><circle cx="5" cy="4" r="1.5" fill="var(--red)"/></svg></span>
        Natural gas<br>transmission industry
      </li>
      <li class="contact-item">
        <span class="contact-icon"><svg width="11" height="11" viewBox="0 0 12 12"><path d="M2.5 0.5l2 2.5-1.2 1.5a7 7 0 0 0 4.2 4.2L9 7.5l2.5 2-1.2 2C5 11 1 7 .5 1.7z" fill="#fff"/></svg></span>
        55501 55501
      </li>
      <li class="contact-item">
        <span class="contact-icon"><svg width="12" height="9" viewBox="0 0 12 9"><rect x=".5" y=".5" width="11" height="8" fill="#fff"/><path d="M.5 .5l5.5 4.5L11.5 .5" fill="none" stroke="var(--red)"/></svg></span>
        HALVARD@MAILBOX.COM
      </li>
    </ul>
  </div>
  <div class="brand-panel">
    <span class="brand-square"></span>
    <span class="brand-name">HVR</span>
  </div>
</section>

</body>
</html>
```